This is for the green Pet RESORT Brochure. It was the original green design created for our Pet SPA Brochure. Thank you!

Pet

• The green designed originally uploaded for the Pet SPA Brochure. The spa brochure ended up being brown, but the green design is perfect for our Pet RESORT Brochure.

```html
<!DOCTYPE html>
<html lang="en">
<head>
<meta charset="utf-8">
<title>Pet Resort Brochure – Accommodations &amp; Amenities</title>
<link href="https://fonts.googleapis.com/css2?family=Cormorant+Garamond:wght@500;600;700&display=swap" rel="stylesheet">
<style>
  :root{
    --bg-light:#eef6d6;
    --bg-green:#a9d266;
    --bg-deep:#7dbb3c;
    --panel:#4c1d2d;
    --panel-edge:#f4efe6;
    --swoosh:#7a4a1e;
    --ink:#ffffff;
    --silhouette:#8b3a14;
  }
  *{box-sizing:border-box;margin:0;padding:0}
  html,body{width:1200px;height:729px;overflow:hidden}
  body{
    position:relative;
    font-family:"Cormorant Garamond",Georgia,serif;
    font-variant:small-caps;
    color:var(--ink);
    background:radial-gradient(ellipse at 55% 15%,var(--bg-light) 0%,var(--bg-green) 55%,var(--bg-deep) 100%);
  }
  .pets{position:absolute;left:240px;top:612px;width:520px;height:117px;z-index:0;pointer-events:none}
  .panel{
    position:absolute;
    z-index:1;
    background:var(--panel);
    border:2px solid var(--panel-edge);
    border-radius:12px;
    box-shadow:0 3px 8px rgba(0,0,0,.35);
    padding:12px 13px;
    font-size:13.2px;
    line-height:1.22;
    font-weight:600;
  }
  .p1{left:27px;top:21px;width:268px;height:693px}
  .p2{left:315px;top:18px;width:268px;height:672px}
  .p3{left:607px;top:18px;width:268px;height:690px}
  .p4{left:901px;top:14px;width:267px;height:688px}
  .section-title{font-size:14px;font-weight:700;margin:6px 0 18px}
  .item{margin-bottom:20px}
  .item-head{display:flex;align-items:baseline;font-weight:700;font-size:13.5px}
  .leader{flex:1;border-bottom:2px dotted var(--ink);margin:0 3px;transform:translateY(-3px)}
  .item-desc{text-align:justify;margin-top:3px}
  .rates{display:grid;grid-template-columns:1fr 1fr;gap:2px 10px;font-weight:700;margin-top:3px}
  .rates span{display:flex;justify-content:space-between}
  .sub-title{font-size:16px;font-weight:600;margin:18px 0 20px}
  strong{font-variant:normal;font-weight:700}
  .swoosh{position:absolute;left:0;top:0;width:1200px;height:729px;z-index:2;pointer-events:none;mix-blend-mode:multiply}
</style>
</head>
<body>

<svg class="pets" viewBox="0 0 520 117" role="img" aria-label="Silhouettes of dogs and cats walking along the bottom edge">
  <rect x="0" y="20" width="520" height="97" rx="30" fill="var(--silhouette)" opacity=".6"/>
</svg>

<section class="panel p1">
  <h2 class="section-title">Canine Accommodations</h2>
  <div class="item">
    <div class="item-head">Comfort Suites<span class="leader"></span>See Below</div>
    <p class="item-desc">Full range of sizes, from 12 square feet (3 x 4) to 35 square feet rooms (5 x 7), with a 4 x 8 to 4 x 12 outside covered patio.</p>
    <div class="rates">
      <span>Under 20lbs <b>$26</b></span><span>81 – 110lbs <b>$32</b></span>
      <span>21 – 50lbs <b>$28</b></span><span>111lbs &amp; Over <b>$34</b></span>
      <span>51 – 80lbs <b>$30</b></span>
    </div>
  </div>
  <div class="item">
    <div class="item-head">Luxury Suites<span class="leader"></span>$60</div>
    <div class="item-head">2 Dogs<span class="leader"></span>$110</div>
    <p class="item-desc">A 42 square foot room (6 x 7) and a 6 x 10 1/2 outside covered terrace. Includes tile floors, a raised bed, a flatscreen TV with cable and a daily Playtime and Treat (a $10.00 value).</p>
    <p class="item-desc">The price (a $7.00 value).</p>
  </div>
  <div class="item">
    <div class="item-head">Day Only Service<span class="leader"></span>$25</div>
    <div class="item-head">2 Dogs<span class="leader"></span>$40</div>
    <p class="item-desc">A Day of Fun, Playtimes, Comfort and Relaxation. Includes a Comfort Suite and several Playtimes throughout the day. Day Only Services can be Group or Individual.</p>
  </div>
</section>

<section class="panel p2">
  <h2 class="section-title">Feline Accommodations</h2>
  <div class="item">
    <div class="item-head">Condos<span class="leader"></span>$18</div>
    <p class="item-desc">A 6 square foot room (2 x 3) with two (2) floors. Depending upon the number of guests staying with us the adjacent Condos can be combined to give a single guest more space to explore.</p>
  </div>
  <div class="item">
    <div class="item-head">Townhomes<span class="leader"></span>$23</div>
    <p class="item-desc">A 5 square foot room (2 ½ x 2 ½) with four (4) floors rising over 7 feet. A daily Playtime is also included in the price (a $7.00 value).</p>
  </div>
  <p class="item-desc">Is available as a Group Amenity. Includes Group Socializing, Activities, Exploring and Fun. <strong>An evaluation and waiver is required</strong>. A customer with multiple pets is only charged for one. Guests from the same household don't require an evaluation and wavier to play with one another.</p>
  <h3 class="sub-title">Canine Amenities</h3>
  <div class="item">
    <div class="item-head">Group Playtime<span class="leader"></span>$7</div>
    <p class="item-desc">Includes group socializing, activities, exploring and fun. An evaluation and waiver is required. Size, age, health and temperament determines the makeup of the group.</p>
  </div>
</section>

<section class="panel p3">
  <div class="item">
    <div class="item-head">Playtime<span class="leader"></span>$7</div>
    <p class="item-desc">15 minutes in one of our dedicated play areas. Includes running, frisbee, ball throwing, tag, tug-o-war and exploring.</p>
  </div>
  <div class="item" style="margin-top:34px">
    <div class="item-head">Walk<span class="leader"></span>$7</div>
    <p class="item-desc">15 minutes on leash in a guided tour around our Pet Resort. Includes talking, petting and of course smelling.</p>
  </div>
  <div class="item" style="margin-top:34px">
    <div class="item-head">Downtime<span class="leader"></span>$10</div>
    <p class="item-desc">20 minutes either outside in the soft grass or inside in a quiet area. Includes cuddling, rub downs and brushing.</p>
  </div>
  <div class="item">
    <div class="item-head">Trot-Along<span class="leader"></span>$10</div>
    <p class="item-desc">20 minutes of warm up, exercise jog on our trot-along treadmill and cool down.</p>
  </div>
  <div class="item">
    <div class="item-head">Trail-Tail Maze<span class="leader"></span>$12</div>
    <p class="item-desc">20 minutes in our Trail-Tail Maze. Includes running and jumping through our Fall Paw or Winter Wonderland Maze in addition to what is included in Playtimes.</p>
  </div>
  <div class="item">
    <div class="item-head">Little Paws Den<span class="leader"></span>$12</div>
    <p class="item-desc">20 minutes in our Seasonally Themed Little Paws Den. Includes themed equipment and fun in addition to what is included in Playtimes.</p>
  </div>
</section>

<section class="panel p4">
  <div class="item">
    <div class="item-head">Lagoon Splash<span class="leader"></span>$15</div>
    <p class="item-desc">20 minutes in our outdoor in ground Lagoon Splash pool. Includes fountains and pool toys in addition to what is included in Playtimes.</p>
  </div>
  <div class="item">
    <div class="item-head">Hydro-Exercise<span class="leader"></span>$25</div>
    <p class="item-desc">20 minutes in our Indoor Heated Endless Lap Pool. Includes toys, none weight bearing exercise and swimming.</p>
  </div>
  <div class="item">
    <div class="item-head">Hydro-Rejuvenation<span class="leader"></span>$35</div>
    <p class="item-desc">20 minutes in our Indoor Heated Endless Lap Pool. Includes none weight bearing exercise, stretching, massage and cooldown.</p>
  </div>
  <div class="item">
    <div class="item-head">Special Treats<span class="leader"></span>$3 Each</div>
    <p class="item-desc">Choose from Treat filled Chewbos (Peanut Butter or Liver) and Chilly Pup Ice Cream Sundaes.</p>
  </div>
  <h3 class="section-title" style="margin-top:8px">Feline Amenities</h3>
  <div class="item">
    <div class="item-head">Playtime<span class="leader"></span>$7</div>
    <p class="item-desc">15 minutes in the cat lounge. Includes mice, feathers, laser pointers, and feline jungle gyms.</p>
  </div>
  <div class="item">
    <div class="item-head">Downtime<span class="leader"></span>$10</div>
    <p class="item-desc">20 minutes in the cat lounge sitting in a rocking chair in front of the bird viewing area. Includes cuddling, rub downs and brushing.</p>
  </div>
</section>

<svg class="swoosh" viewBox="0 0 1200 729" aria-hidden="true">
  <path d="M0 270 C180 170 420 190 580 330 C680 420 760 560 820 729 L0 729 Z" fill="var(--swoosh)" opacity=".55"/>
</svg>

</body>
</html>
```